Label Design

Our company is looking for someone to design a label for our juice bottles. We need 1 design that can be edited and used for four different juice combinations. We are a local juice shop that sales fruit and vegetable juices. We would like to see designs that outline the name of the juices, ingredients included within the juice, and size of the bottle. The dimensions of our bottles are 9.67 inches height x 1.97inches width. We are looking for something that is simple yet eye catching.

```html
<!DOCTYPE html>
<html lang="en">
<head>
<meta charset="utf-8">
<title>Quenching Ruby – Juice Bottle Label</title>
<link href="https://fonts.googleapis.com/css2?family=Righteous&family=Roboto:wght@400&display=swap" rel="stylesheet">
<style>
  :root {
    --deep-red: #9c0b0b;
    --bright-red: #e42323;
    --leaf-green: #2e8540;
    --brand-orange: #e8782f;
    --dim-blue: #3a7bb5;
    --ink: #222222;
    --paper: #ffffff;
  }
  html, body {
    margin: 0;
    padding: 0;
    width: 1200px;
    height: 1199px;
    overflow: hidden;
    background: var(--paper);
  }
  .artboard { display: block; width: 1200px; height: 1199px; }
  .label-text { font-family: "Righteous", sans-serif; }
  .dimension-text { font-family: "Roboto", sans-serif; fill: var(--dim-blue); font-size: 50px; }
  .dimension-line { stroke: var(--dim-blue); stroke-width: 1.5; fill: none; }
  .dimension-arrow { fill: var(--dim-blue); }
  .band-bright { fill: var(--bright-red); }
  .band-deep { fill: var(--deep-red); }
  .brand-name { fill: var(--brand-orange); font-size: 62px; }
  .product-name { fill: var(--deep-red); font-size: 118px; }
  .ingredients { fill: var(--leaf-green); font-size: 32px; }
  .juice-type { fill: var(--deep-red); font-size: 25px; }
  .volume { fill: var(--paper); font-size: 30px; }
  .care-note { fill: var(--paper); font-size: 18px; }
  .date-note { fill: var(--ink); font-size: 16px; }
</style>
</head>
<body>
<svg class="artboard" viewBox="0 0 1832 1832" preserveAspectRatio="none" xmlns="http://www.w3.org/2000/svg">
  <defs>
    <linearGradient id="juice-splash" x1="0" y1="1" x2="1" y2="0">
      <stop offset="0" stop-color="#f6b73c" stop-opacity="0.85"/>
      <stop offset="0.5" stop-color="#f0a21c" stop-opacity="0.6"/>
      <stop offset="1" stop-color="#e58a12" stop-opacity="0.85"/>
    </linearGradient>
  </defs>

  <g class="dimension-width">
    <line class="dimension-line" x1="698" y1="405" x2="698" y2="500"/>
    <line class="dimension-line" x1="1290" y1="405" x2="1290" y2="500"/>
    <line class="dimension-line" x1="740" y1="435" x2="930" y2="435"/>
    <line class="dimension-line" x1="1068" y1="435" x2="1248" y2="435"/>
    <polygon class="dimension-arrow" points="698,435 744,423 744,447"/>
    <polygon class="dimension-arrow" points="1290,435 1244,423 1244,447"/>
    <text class="dimension-text" x="998" y="453" text-anchor="middle">1.97"</text>
  </g>

  <g class="dimension-height">
    <line class="dimension-line" x1="556" y1="516" x2="668" y2="516"/>
    <line class="dimension-line" x1="556" y1="1440" x2="668" y2="1440"/>
    <line class="dimension-line" x1="586" y1="558" x2="586" y2="905"/>
    <line class="dimension-line" x1="586" y1="1050" x2="586" y2="1398"/>
    <polygon class="dimension-arrow" points="586,516 574,562 598,562"/>
    <polygon class="dimension-arrow" points="586,1440 574,1394 598,1394"/>
    <text class="dimension-text" x="0" y="0" text-anchor="middle" transform="translate(604,975) rotate(-90)">3.08"</text>
  </g>

  <g class="label label-text">
    <rect x="698" y="516" width="592" height="924" fill="var(--paper)"/>

    <path class="band-bright" d="M698,516 H1290 V618 C1200,650 1050,665 950,662 C830,662 750,700 698,735 Z"/>
    <path class="band-deep" d="M698,516 H1290 V583 C1200,620 1050,640 950,640 C830,645 750,680 698,712 Z"/>

    <text class="brand-name" x="992" y="630" text-anchor="middle">Fortuna Juices</text>

    <text class="product-name" x="740" y="868" textLength="508" lengthAdjust="spacingAndGlyphs">Quenching</text>
    <text class="product-name" x="993" y="963" text-anchor="middle">Ruby</text>

    <path role="img" aria-label="Splash of golden juice with scattered droplets"
      fill="url(#juice-splash)"
      d="M728,1300 C780,1250 850,1215 910,1220 C960,1225 990,1290 1000,1320 L1040,1310 C1020,1260 990,1220 1005,1190 C1030,1215 1080,1230 1120,1180 C1150,1140 1180,1110 1220,1140 C1260,1170 1275,1210 1270,1240 C1240,1280 1210,1300 1180,1320 L800,1335 C790,1315 760,1305 728,1300 Z"/>

    <text class="ingredients" x="730" y="1087" textLength="528" lengthAdjust="spacingAndGlyphs">Apple | Basil | Watermelon | Zucchini</text>
    <text class="juice-type" x="853" y="1122" textLength="281" lengthAdjust="spacingAndGlyphs">Fruit &amp; Vegetable Juice</text>

    <text class="date-note" x="0" y="0" transform="translate(716,1326) rotate(-90)">Drink/Freeze by</text>

    <path class="band-bright" d="M698,1345 C800,1305 1000,1300 1100,1296 C1200,1290 1260,1250 1290,1220 V1440 H698 Z"/>
    <path class="band-deep" d="M698,1376 C800,1335 1000,1325 1100,1312 C1200,1300 1260,1265 1290,1238 V1440 H698 Z"/>

    <text class="volume" x="872" y="1375" textLength="244" lengthAdjust="spacingAndGlyphs">12 FL OZ (355ML)</text>
    <text class="care-note" x="711" y="1427" textLength="279" lengthAdjust="spacingAndGlyphs">Keep Refrigerated &amp; Shake Well</text>
    <text class="care-note" x="1038" y="1427" textLength="238" lengthAdjust="spacingAndGlyphs">Perishable, Not pasteurized</text>
  </g>
</svg>
</body>
</html>
```